Whey Protein Packet Label Design

Company background:

Company name: Fernwick Vale

Website: fernwickvale-example.com

Summary: We offer single serving supplements on the go that are all natural. We are all about healthy living and portable packaging that makes it easy to drink anywhere. Our Whey Protein Packet saves time and is convenient for our customers to make a protein shake anywhere, there is no prep time, cook time, or clean up time. These protein packets can be added into any shaker and it is easily mixed, no more large bulk tubs of protein needed anymore because we offer single servings that are manageable to carry around.

Style: Our company name is Fernwick Vale, so in our logo we are saying that anyone can reach the mountain peak by taking healthy foods. That somehow needs to be shown through a pattern or something.

Products: Whey Protein Packets, Energy Sticks, Recovery Sticks

Product Label Instruction:

I need a product label for the Whey Protein Packet for 5 flavors.
-There should be one generic design, and the flavors just change according to color scheme and pictures

1. Strawberry Banana Smoothie (100% Organic Fruit Powder)
color scheme: Red, white, brown
2. Peanut Butter Smoothie (100% Organic Nut Powder)
color scheme: light brown, brown, white
3. Chocolate Smoothie(100% Organic Cacao Powder)
color scheme: dark brown, brown, white
4. Vanilla Shake (100% Pure Vanilla Powder)
color scheme: light cream, brown, white
5. Banana Peanut Butter Shake (100% Organic Fruit & Nut Powder)
color scheme: yellow, brown, white

Each flavor label design should have this text/information on the front:

1. Logo (attached) - does not need to be main part of design( just placed somewhere is fine)
2. Natural Whey Protein Packet (product title)
3. Flavor Name
4. Flavor Picture
5. 30G (amount of protein in each packet)
6. 4 professional stamps that easily state (attached an image for example)
1. Non GMO
2. Gluten Free
3. Lactose Free
4. No Artificial Flavoring
7. Net Weight 36G

Colors: I would like to use flavor color, brown, and white mainly for the packaging but I am open to different colors for diff flavors and colorful pictures.

Ideas: Please give me multiple designs to look at for the first draft.

Other company examples: I have attached some pictures of other packaging designs that I like that you can keep in mind.

Target Market(s)

Upscale, organic lifestyle, vegans, on the go people, police force, outdoor people, health junkies, gym goers, men and women

I hope you can make something that will appeal to most or all of these categories.

Industry/Entity Type

It Company

Requirements
Must have
• label dimensions: 3 x 3.75
• font: Unique, not something basic that looks like it came off of word document. It needs to look professional and unique that the upscale market would like.
Nice to have
• I have attached some examples of other companies that I like the look of. That is the type of style I am going for.
Should not have
• It should not be a basic design that I can make myself. I am looking for a professional who can make the product look like an organic style and shows that we offer HIGH QUALITY, high end supplements.

```html
<!DOCTYPE html>
<html lang="en">
<head>
<meta charset="utf-8">
<title>Fernwick Vale – Natural Whey Protein Packet</title>
<link href="https://fonts.googleapis.com/css2?family=Antonio:wght@200;300&family=Josefin+Sans:wght@400;600&display=swap" rel="stylesheet">
<style>
  :root {
    --backdrop: #d9d9d9;
    --label-white: #f7f7f7;
    --flavor-red: #d42a32;
    --brown: #5a2a22;
    --stamp-grey: #6e6e70;
    --stamp-ink: #f2f2f2;
  }
  html, body {
    margin: 0;
    width: 1200px;
    height: 1200px;
    overflow: hidden;
    background: var(--backdrop);
  }
  .label {
    position: absolute;
    left: 260px;
    top: 95px;
    width: 680px;
    height: 1010px;
    background: var(--label-white);
    overflow: hidden;
  }
  .cliff-photo {
    position: absolute;
    left: 0;
    top: 0;
    width: 300px;
    height: 1010px;
  }
  .brand {
    position: absolute;
    right: 58px;
    top: 74px;
    display: flex;
    align-items: center;
    gap: 10px;
    font-family: "Josefin Sans", sans-serif;
    font-weight: 400;
    font-size: 30px;
    letter-spacing: 1px;
    text-transform: uppercase;
    color: var(--flavor-red);
    white-space: nowrap;
  }
  .brand-dot {
    width: 12px;
    height: 12px;
    border-radius: 50%;
    background: var(--flavor-red);
  }
  .product-title {
    position: absolute;
    right: 60px;
    top: 210px;
    margin: 0;
    text-align: right;
    font-family: "Antonio", sans-serif;
    font-weight: 200;
    font-size: 68px;
    line-height: 80px;
    letter-spacing: -0.5px;
    color: var(--brown);
    text-transform: uppercase;
    white-space: nowrap;
    transform: scaleX(0.88);
    transform-origin: right top;
  }
  .flavor-band {
    position: absolute;
    left: 238px;
    right: 0;
    top: 560px;
    height: 228px;
    background: var(--flavor-red);
    color: #fff;
    font-family: "Josefin Sans", sans-serif;
  }
  .flavor-band .inner {
    position: absolute;
    right: 70px;
    top: 32px;
    width: 300px;
    text-align: right;
  }
  .flavor-name {
    margin: 0;
    font-weight: 600;
    font-size: 30px;
    line-height: 38px;
    text-transform: uppercase;
    white-space: nowrap;
    padding-bottom: 8px;
    border-bottom: 2px solid #fff;
  }
  .flavor-note {
    margin: 0 0 0 160px;
    padding: 12px 0 6px;
    font-size: 20px;
    line-height: 26px;
    white-space: nowrap;
    border-bottom: 2px solid #fff;
  }
  .flavor-note span { display: inline-block; margin-left: -160px; }
  .net-weight {
    margin: 10px 0 0;
    font-size: 18px;
    line-height: 22px;
    text-transform: uppercase;
    white-space: nowrap;
  }
  .stamps {
    position: absolute;
    left: 198px;
    top: 802px;
    display: flex;
    gap: 8px;
  }
  .stamp { width: 100px; height: 100px; }
  .stamp text {
    font-family: "Josefin Sans", sans-serif;
    font-size: 11px;
    fill: var(--stamp-ink);
    text-anchor: middle;
  }
  .stamp line { stroke: var(--stamp-ink); stroke-width: 1.3; }
</style>
</head>
<body>
  <main class="label">
    <svg class="cliff-photo" viewBox="0 0 300 1010" role="img" aria-label="Photograph of a red-toned rock cliff with a climber ascending on a rope">
      <defs>
        <linearGradient id="cliffTone" x1="0" y1="0" x2="1" y2="1">
          <stop offset="0" stop-color="#c41820"/>
          <stop offset="0.5" stop-color="#b5121b"/>
          <stop offset="1" stop-color="#7e0c12"/>
        </linearGradient>
      </defs>
      <path d="M0 0 H298 Q296 200 292 380 Q290 500 286 600 Q250 800 218 1010 H0 Z" fill="url(#cliffTone)"/>
    </svg>

    <div class="brand"><span class="brand-dot"></span>Fernwick Vale</div>

    <h1 class="product-title">Natural Whey<br>Protein Packet</h1>

    <section class="flavor-band">
      <div class="inner">
        <h2 class="flavor-name">Strawberry<br>Banana Smoothie</h2>
        <p class="flavor-note"><span>(100% Organic Fruit Powder)</span></p>
        <p class="net-weight">Net Wt.: 30G</p>
      </div>
    </section>

    <section class="stamps">
      <svg class="stamp" viewBox="0 0 100 100" aria-label="Non GMO">
        <circle cx="50" cy="50" r="48" fill="var(--stamp-grey)"/>
        <circle cx="50" cy="50" r="42" fill="none" stroke="var(--stamp-ink)" stroke-width="1.3"/>
        <g transform="rotate(-17 50 50)">
          <line x1="12" y1="40" x2="88" y2="40"/>
          <line x1="12" y1="60" x2="88" y2="60"/>
          <text x="50" y="54">NON GMO</text>
        </g>
      </svg>
      <svg class="stamp" viewBox="0 0 100 100" aria-label="Gluten Free">
        <circle cx="50" cy="50" r="48" fill="var(--stamp-grey)"/>
        <circle cx="50" cy="50" r="42" fill="none" stroke="var(--stamp-ink)" stroke-width="1.3"/>
        <g transform="rotate(-17 50 50)">
          <line x1="12" y1="40" x2="88" y2="40"/>
          <line x1="12" y1="60" x2="88" y2="60"/>
          <text x="50" y="54">GLUTEN FREE</text>
        </g>
      </svg>
      <svg class="stamp" viewBox="0 0 100 100" aria-label="Lactose Free">
        <circle cx="50" cy="50" r="48" fill="var(--stamp-grey)"/>
        <circle cx="50" cy="50" r="42" fill="none" stroke="var(--stamp-ink)" stroke-width="1.3"/>
        <g transform="rotate(-17 50 50)">
          <line x1="12" y1="40" x2="88" y2="40"/>
          <line x1="12" y1="60" x2="88" y2="60"/>
          <text x="50" y="54">LACTOSE FREE</text>
        </g>
      </svg>
      <svg class="stamp" viewBox="0 0 100 100" aria-label="No Artificial Flavoring">
        <circle cx="50" cy="50" r="48" fill="var(--stamp-grey)"/>
        <circle cx="50" cy="50" r="42" fill="none" stroke="var(--stamp-ink)" stroke-width="1.3"/>
        <g transform="rotate(-20 50 50)">
          <line x1="14" y1="35" x2="86" y2="35"/>
          <line x1="14" y1="66" x2="86" y2="66"/>
          <text x="50" y="48" style="font-size:10px">NO ARTIFICIAL</text>
          <text x="50" y="60" style="font-size:10px">FLAVORING</text>
        </g>
      </svg>
    </section>
  </main>
</body>
</html>
```